Web Design for Rubbish Removal Company

I am looking for a custom web design that is clean and modern which also has a professional trustworthy feel to it.
The website is http://www.kendrawaste.com.au/ and need:
1 x Front Page
1 x Location Page
Please keep the green colour scheme as this is the corporate colours but would like to steer away from the black.
Industry/Entity Type
It Company
Number of Pages Required
2 page
Font styles to use
Sans Serif
Requirements
Must have
- Clean & Professional
- Keep green colour scheme
Should not have
- Steer away from black
- not look like a template

```html
<!DOCTYPE html>
<html lang="en">
<head>
<meta charset="utf-8">
<title>Kendra Waste Removal</title>
<link href="https://fonts.googleapis.com/css2?family=Arimo:wght@400;700&family=Open+Sans:wght@400&display=swap" rel="stylesheet">
<style>
  :root {
    --green: #6cbf45;
    --green-text: #5cb53f;
    --blue: #1b70c2;
    --grey: #d4d4d6;
    --white: #ffffff;
  }
  * { box-sizing: border-box; margin: 0; padding: 0; }
  html, body { width: 800px; height: 1200px; overflow: hidden; background: var(--white); }
  .page { position: relative; width: 800px; height: 1200px; font-family: "Arimo", Arial, sans-serif; }

  .site-header { position: absolute; left: 0; top: 0; width: 800px; height: 180px; background: var(--green); }
  .brand { position: absolute; left: 38px; top: 28px; color: var(--white); font-weight: 700; }
  .brand-name { font-size: 72px; line-height: 1; letter-spacing: 3px; }
  .brand-tag { font-size: 26px; letter-spacing: 3px; margin-top: 12px; }
  .header-visual { position: absolute; left: 474px; top: 0; width: 326px; height: 160px; background: var(--white); padding: 10px 14px 14px; }
  .header-visual div { width: 100%; height: 100%; background: linear-gradient(180deg, #eef2ee 0%, #3f7a3a 45%, #cfd3d6 100%); }

  .main-nav { position: absolute; left: 28px; top: 180px; width: 748px; height: 40px; display: flex; gap: 4px; }
  .main-nav a { flex: auto; background: var(--blue); color: var(--white); text-decoration: none; font-weight: 700; font-size: 14px; display: flex; align-items: center; justify-content: center; }

  .visual { position: absolute; }
  .intro-visual { left: 90px; top: 262px; width: 220px; height: 220px; background: linear-gradient(180deg, #e9d7c8 0%, #6cbf45 55%, #e4e4e4 100%); }
  .bins-visual { left: 56px; top: 530px; width: 244px; height: 160px; background: linear-gradient(90deg, #2b6fc9 0%, #6cbf45 40%, #f2e531 65%, #d93a3a 100%); }
  .mascot-visual { left: 400px; top: 748px; width: 370px; height: 154px; background: linear-gradient(180deg, #4a4f56 0%, #2e6fc2 55%, #f1f1f1 100%); }
  .recycle-visual { left: 532px; top: 940px; width: 128px; height: 144px; background: radial-gradient(circle, #9aa0a6 0%, #2f9a4a 70%, #ffffff 100%); }

  .copy { position: absolute; font-family: "Open Sans", Arial, sans-serif; font-size: 15px; line-height: 22px; color: var(--green-text); }
  .copy-intro { left: 322px; top: 334px; width: 440px; }
  .copy-app { left: 322px; top: 540px; width: 440px; }

  .contact-form { position: absolute; left: 10px; top: 716px; width: 366px; height: 398px; background: var(--grey); }
  .field { position: absolute; left: 26px; width: 330px; background: var(--green); color: var(--white); font-weight: 700; font-size: 16px; padding: 0 16px; border: 2px solid var(--white); }
  .field-name { top: 22px; height: 46px; line-height: 42px; }
  .field-email { top: 78px; height: 46px; line-height: 42px; }
  .field-phone { top: 134px; height: 46px; line-height: 42px; }
  .field-message { top: 196px; height: 126px; padding-top: 8px; }
  .submit { position: absolute; left: 26px; top: 332px; width: 330px; height: 40px; background: var(--blue); color: var(--white); font-weight: 700; font-size: 16px; display: flex; align-items: center; justify-content: center; }

  .site-footer { position: absolute; left: 0; top: 1132px; width: 800px; height: 68px; background: var(--green); }
  .site-footer a { position: absolute; top: 24px; color: var(--white); text-decoration: none; font-weight: 700; font-size: 18px; }
</style>
</head>
<body>
<div class="page">
  <header class="site-header">
    <div class="brand">
      <div class="brand-name">KENDRA</div>
      <div class="brand-tag">WASTE REMOVAL</div>
    </div>
    <div class="header-visual"><div role="img" aria-label="Green junk hauling truck"></div></div>
  </header>

  <nav class="main-nav">
    <a href="#">HOME</a><a href="#">ABOUT</a><a href="#">SERVICES</a><a href="#">GALLERY</a><a href="#">FAQS</a><a href="#">TESTIMONIALS</a><a href="#">LOCATIONS</a><a href="#">BLOG</a><a href="#">CONTACT</a>
  </nav>

  <div class="visual intro-visual" role="img" aria-label="Smiling worker in a green shirt and apron giving a thumbs up"></div>
  <p class="copy copy-intro">We like to call it the Findly of recycling, that's its first primary purpose; this is a classic case of parallel thinking. GreenLoop's creators are currently preparing for its national launch, which is set for sometime next month. Ridgeford's binwise already has 2,500 users, and the city hopes to share in the near future.</p>

  <div class="visual bins-visual" role="img" aria-label="Row of colourful recycling bins for paper, glass, plastic and metal"></div>
  <p class="copy copy-app">The city of Ridgeford introduced a new recycling app for smartphones last month, called binwise. The app provides answers to several common questions regarding the recycling process and containers. One of the most notable features of binwise is a search function that allows users to learn the recycling rules for specific products.</p>

  <form class="contact-form">
    <div class="field field-name">NAME</div>
    <div class="field field-email">EMAIL</div>
    <div class="field field-phone">PHONE NO</div>
    <div class="field field-message">MASSEGE</div>
    <div class="submit">SUBMITE</div>
  </form>

  <div class="visual mascot-visual" role="img" aria-label="Cartoon wheelie bins in snow holding a shovel"></div>
  <div class="visual recycle-visual" role="img" aria-label="Bin inside green recycling arrows"></div>

  <footer class="site-footer">
    <a href="#" style="left:142px">CONTACT US</a>
    <a href="#" style="left:348px">SEARCH</a>
    <a href="#" style="left:538px">COMMENT</a>
  </footer>
</div>
</body>
</html>
```